Redesign of page from emergency manual

Please redesign this PDF to look better. Please don't include any stock photos. It must be legible. Making some words bold is probably a good idea.

Here are some things I like :

https://tarrowbooks.com.au/collections/frontpage/products/the-plk-v2-ebook

https://img-cd.vostramediafiles.com/qa-ejkwPLOTYY_SuCKbZNu411Qwgjv8YssPxEdzXN93hDkSRjLXK8WmfgbmrJW4ZZ3yUPK=w1052-h592-rw

```html
<!DOCTYPE html>
<html lang="en">
<head>
<meta charset="utf-8">
<title>Hypertension Acute – Emergency Manual Page</title>
<link rel="stylesheet" href="https://fonts.googleapis.com/css2?family=Montserrat:wght@400;500;600;700;800;900&display=swap">
<style>
  :root{
    --blue:#0b62ac;
    --sky:#4fb8e6;
    --yellow:#ffdd00;
    --red:#e2101a;
    --cream:#fffbd6;
    --grey:#efefef;
    --ink:#1a1a1a;
    --paper:#ffffff;
    --backdrop:#e9e9e9;
  }
  *{box-sizing:border-box;margin:0;padding:0}
  html,body{width:1200px;height:614px;overflow:hidden;background:var(--backdrop)}
  body{font-family:"Montserrat",sans-serif;color:var(--ink)}
  .page{position:absolute;left:394px;top:17px;width:412px;height:580px;background:var(--paper);box-shadow:0 2px 10px rgba(0,0,0,.15);overflow:hidden}
  .header{position:absolute;left:0;top:0;width:412px;height:119px;background:var(--blue)}
  .title{position:absolute;left:16px;top:16px;font-weight:900;font-size:33px;line-height:31px;color:#fff;letter-spacing:.3px}
  .revision{position:absolute;right:14px;top:20px;font-size:6px;line-height:9px;letter-spacing:1.2px;color:#fff;font-weight:500}
  .subtitle-band{position:absolute;left:0;top:84px;width:270px;height:35px}
  .subtitle{position:absolute;left:15px;top:90px;font-size:11.2px;line-height:11.6px;font-weight:500;color:var(--ink)}
  .intro{position:absolute;left:16px;top:134px;width:184px;font-size:7.6px;line-height:10.8px}
  .intro .lead{padding-left:10px;position:relative}
  .intro .lead::before{content:"";position:absolute;left:0;top:2px;border-left:5px solid var(--blue);border-top:3px solid transparent;border-bottom:3px solid transparent}
  .intro .check{color:var(--blue);font-weight:600;padding-left:15px;text-indent:-5px;margin-top:9px}
  .intro .note{font-size:6.2px;padding-left:10px;margin-top:9px}
  .bp-table{position:absolute;left:211px;top:136px;width:181px;border-collapse:collapse;font-size:8px;text-align:center;border:1px solid var(--blue)}
  .bp-table caption{background:var(--red);color:#fff;font-weight:700;font-size:8px;padding:5px 0;border:1px solid var(--blue);border-bottom:none}
  .bp-table th{background:var(--sky);color:#fff;font-weight:600;height:19px;border-left:1px solid var(--blue)}
  .bp-table td{height:18.5px;border-top:1px solid var(--blue);border-left:1px solid var(--blue)}
  .bp-table tr.alt td{background:var(--cream)}
  .caution{position:absolute;left:20px;top:254px;width:370px;height:46px;background:var(--grey);padding:8px 7px;font-size:7.1px;line-height:10px;text-align:justify}
  .caution strong{color:var(--red);font-weight:700}
  .drug-table{position:absolute;left:20px;top:310px;width:368px;table-layout:fixed;border-collapse:collapse;font-size:7.4px;border:1px solid var(--blue)}
  .drug-table th{color:#fff;font-weight:600;font-size:8.6px;height:20px}
  .drug-table th.action{background:var(--blue);width:117px}
  .drug-table th.drug{background:var(--red)}
  .drug-table td{border-top:1px solid var(--blue);vertical-align:top;padding:6px 6px 4px 12px;line-height:10px}
  .drug-table td.action{border-right:1px solid var(--blue);font-weight:600;font-size:7.6px}
  .drug-table tr.alt td{background:var(--cream)}
  .drug-table tr.row-short{height:34px}
  .drug-table tr.row-tall{height:52px}
  .drug-table tr.row-mid{height:37px}
  .drug-table tr.row-single{height:24px}
  .drug-table ul{list-style:none}
  .drug-table li,.diff li{position:relative;padding-left:13px}
  .drug-table li+li{margin-top:3px}
  .drug-table li::before,.diff li::before{content:"";position:absolute;left:2px;top:2px;border-left:5px solid var(--red);border-top:3px solid transparent;border-bottom:3px solid transparent}
  .diff-heading{position:absolute;left:20px;top:491px;width:368px;display:flex;align-items:center;gap:12px;color:var(--blue);font-weight:800;font-size:10.5px;line-height:13px;letter-spacing:.3px;white-space:nowrap}
  .diff-heading::before,.diff-heading::after{content:"";flex:1;height:1.5px;background:var(--blue)}
  .diff{position:absolute;top:511px;list-style:none;font-size:7.2px;line-height:10px}
  .diff li{margin-bottom:2px}
  .diff.col1{left:24px;width:120px}
  .diff.col2{left:154px;width:120px}
  .diff.col3{left:288px;width:110px}
  .footer-band{position:absolute;left:0;bottom:0;width:412px;height:8px}
</style>
</head>
<body>
  <article class="page">
    <header>
      <div class="header"></div>
      <svg class="subtitle-band" viewBox="0 0 270 35" preserveAspectRatio="none" aria-hidden="true">
        <polygon points="0,0 240,0 270,35 0,35" fill="var(--yellow)"/>
      </svg>
      <h1 class="title">HYPERTENSION<br>ACUTE</h1>
      <p class="revision">REVISION<br>FEB 2020</p>
      <p class="subtitle">Sustained high blood pressure refractory<br>to treating reversible causes</p>
    </header>

    <section class="intro">
      <p class="lead">In pediatrics, hypertension is almost always treated by addressing likely causes such as light anesthesia or measurement error:</p>
      <p class="check">• Ensure correct BP cuff size: cuff bladder width ~ 40% of limb circumference</p>
      <p class="check">• Ensure arterial line transducer is at level of heart</p>
      <p class="note">- Consider placing arterial line if not already present</p>
    </section>

    <table class="bp-table">
      <caption>Hypertensive Blood Pressure Range*</caption>
      <thead><tr><th>Age (yr)</th><th>Systolic</th><th>Diastolic</th></tr></thead>
      <tbody>
        <tr><td>Newborn</td><td>&gt;97</td><td>&gt;70</td></tr>
        <tr class="alt"><td>1-3</td><td>&gt;105</td><td>&gt;61</td></tr>
        <tr><td>4-12</td><td>&gt;113</td><td>&gt;86</td></tr>
      </tbody>
    </table>

    <p class="caution"><strong>CAUTION:</strong> Anti-hypertensive drugs are almost never needed for routine pediatric cases. These medications are used almost exclusively for specialized cardiac, neurosurgical, or endocrine (pheochromocytoma) cases. Consult an expert before use. Rule-out increased ICP.</p>

    <table class="drug-table">
      <thead><tr><th class="action">Action</th><th class="drug">Drug (IV Dosing)</th></tr></thead>
      <tbody>
        <tr class="row-short"><td class="action">Direct smooth muscle<br>relaxation</td><td><ul><li>Sodium nitroprusside 0.5-10 MICROgrams/kg/min</li><li>HydrALAZINE 0.1-0.2 mg/kg (adult dose 5-10 mg)</li></ul></td></tr>
        <tr class="alt row-tall"><td class="action">β-Adrenergic<br>blockade</td><td><ul><li>Esmolol 100-500 MICROgrams/kg over 5 min, then<br>25-300 MICROgrams/kg/min</li><li>Labetalol (also a effect) 0.2-1 mg/kg q 10 min;<br>0.4-3 mg/kg/hour (infusion)</li></ul></td></tr>
        <tr class="row-mid"><td class="action">Calcium channel<br>blockade</td><td><ul><li>niCARdapine 0.5-5 MICROgrams/kg/min</li><li>Clevidipine 0.5-3.5 MICROgrams/kg/min</li></ul></td></tr>
        <tr class="alt row-single"><td class="action">D1-dopamine agonist</td><td><ul><li>Fenoldopam 0.2-0.8 MICROgrams/kg/min</li></ul></td></tr>
      </tbody>
    </table>

    <h2 class="diff-heading">CONSIDER DIFFERENTIAL (PARTIAL)</h2>
    <ul class="diff col1">
      <li>Light anesthesia (consider vaporizer or infusion pump empty or malfunctioning)</li>
      <li>Hypercarbia</li>
    </ul>
    <ul class="diff col2">
      <li>Hypoxemia</li>
      <li>Arterial line transducer too low or BP cuff too small</li>
      <li>Withdrawal (EtOH or opioid)</li>
    </ul>
    <ul class="diff col3">
      <li>Thyroid Storm</li>
      <li>Pheochromocytoma</li>
      <li>Drug Error</li>
    </ul>

    <svg class="footer-band" viewBox="0 0 412 8" preserveAspectRatio="none" aria-hidden="true">
      <polygon points="0,0 129,0 125,8 0,8" fill="var(--blue)"/>
      <polygon points="129,0 286,0 282,8 125,8" fill="var(--yellow)"/>
      <polygon points="286,0 412,0 412,8 282,8" fill="var(--red)"/>
    </svg>
  </article>
</body>
</html>
```